Website Design for Marvane Equity Partners

I am looking to create a website with 3-4 pages for Marvane Equity Partners, a private investment holding company. We already have a logo created via PixelHarbor and would like to incorporate the same dark navy blue color scheme as well as white and potentially other colors including variants of blue, black, and white. We are looking for a conservative, polished design befitting a financial services firm. Our focus as a firm is on identifying opportunities in the overlooked - seeing opportunity where institutional investment is lacking. We are focused on building value for the long-term. We will provide virtually all of the text content but need assistance in setting up the layout, font, design, theme, graphics, etc. The initial three pages will be: Home Page / About Us, "Team", and "Portfolio". Right now, we do not have any portfolio companies but will likely have one within the next several months. The main content page will be the home page. The Team and Portfolio pages will be abbreviated. This website will be expository and is not primarily focused on lead generation or sales.

Ideally, we can incorporate some form of animations / transitions for titles and text sections and stock images (or ideally looped videos) of major city skylines in the U.S. , Latin America, and Europe as those regions are our core investment geographies.

Websites we like that you can use for references include many major private equity firms including Quarrystone Equity (https://www.quarrystoneequity.example/), Briarvale (https://briarvale.example/), KRU Holdings (https://www.kruholdings.example/), and Halvorwick (https://www.halvorwick.example/)
Updates

All,

Thank you to everyone who has posted the initial drafts of the Marvane Equity Partners website. The designs are very good. We would now like to review more refined drafts of our website from the designers.

We have posted updated, specific guidance on website page design and text. Please reference the new uploaded "Marvane Equity Partners Website Design Guidance" Microsoft Word document to refine your submissions.

Thank you!
Ferdinand

Target Market(s)

Investment Professionals

Industry/Entity Type

Financial Services

Coding

Coded - Design and coding required

Number of Pages Required

4 page

```html
<!DOCTYPE html>
<html lang="en">
<head>
<meta charset="utf-8">
<title>Marvane Equity Partners</title>
<link href="https://fonts.googleapis.com/css2?family=Poppins:wght@300;400;500;600;700;800&display=swap" rel="stylesheet">
<style>
:root{
  --navy:#0b1f4f;
  --navy-deep:#08193f;
  --ink:#101a33;
  --muted:#8a8f99;
  --body:#555b66;
  --band:#f1f2f5;
  --footer:#e9ebee;
  --white:#ffffff;
  --rule:#1c2230;
}
*{box-sizing:border-box;margin:0;padding:0}
html,body{width:1200px;height:4751px;overflow:hidden;background:var(--white)}
body{position:relative;font-family:'Poppins',sans-serif;color:var(--ink)}
.abs{position:absolute}
.label{font-size:16px;font-weight:700;letter-spacing:.3px;color:var(--muted);text-transform:uppercase}
.heading{font-size:30px;font-weight:800;color:var(--navy);line-height:1.15;letter-spacing:-.2px}
.copy{font-size:14px;line-height:24px;color:var(--body)}
.photo{position:absolute}

/* header */
.site-header{left:0;top:0;width:1200px;height:74px;background:var(--white)}
.brand{position:absolute;left:48px;top:26px;font-size:20px;font-weight:600;letter-spacing:2px;color:var(--navy);text-transform:uppercase}
.main-nav a{position:absolute;top:30px;font-size:14px;font-weight:500;color:var(--ink);text-decoration:none}
.main-nav a.active::before{content:"";position:absolute;left:0;right:0;top:-30px;height:4px;background:var(--navy)}
.phone-box{position:absolute;left:1124px;top:0;width:76px;height:74px;background:var(--navy);display:flex;align-items:center;justify-content:center}

/* hero */
.hero{left:0;top:74px;width:1200px;height:538px;background:linear-gradient(180deg,#3d5780 0%,#6e7a8c 30%,#5a4a3a 60%,#2e2a22 100%)}
.hero-title{position:absolute;left:0;width:1200px;top:150px;text-align:center;font-size:48px;font-weight:800;line-height:58px;color:var(--white);text-transform:uppercase}
.btn-solid{position:absolute;left:496px;top:293px;width:208px;height:49px;background:var(--navy);border:2px solid var(--white);color:var(--white);font-size:15px;font-weight:700;display:flex;align-items:center;justify-content:center;text-transform:uppercase}

/* about */
.about-label{left:0;width:1200px;top:700px;text-align:center}
.about-heading{left:0;width:1200px;top:730px;text-align:center;font-size:29px;font-weight:700;color:var(--navy)}
.about-copy{left:260px;width:680px;top:786px;text-align:center;font-size:14px;line-height:24px;color:var(--body)}
.stat{position:absolute;top:928px;text-align:center}
.stat b{display:block;font-size:86px;font-weight:300;color:var(--navy);line-height:100px}
.stat span{display:block;font-size:15px;color:var(--navy);margin-top:2px}

/* who we are */
.who-band{left:0;top:1135px;width:1200px;height:603px;background:var(--band)}
.bar-copy{border-left:2px solid var(--ink);padding-left:22px}
.btn-line{position:absolute;border:1.5px solid var(--ink);font-size:14px;font-weight:700;display:flex;align-items:center;justify-content:center;text-transform:uppercase;color:var(--navy)}

/* services */
.service{position:absolute;top:2059px;width:210px}
.service h3{position:absolute;top:97px;left:0;font-size:19px;font-weight:700;color:var(--navy);line-height:25px}
.service p{position:absolute;top:162px;left:0;font-size:14px;line-height:21px;color:#a0a4ab}

/* why */
.why-band{left:0;top:2414px;width:1200px;height:548px;background:var(--navy)}
.why .label{color:#a6acb9}
.why .heading{color:var(--white)}
.why .bar-copy{border-color:var(--white);color:#e6e9ef}
.why .btn-line{border-color:var(--white);color:var(--white)}

/* news */
.news-card{position:absolute;top:3203px;width:258px}
.news-card .photo{left:0;top:0;width:258px;height:312px}
.news-card h4{position:absolute;top:332px;left:0;width:280px;font-size:20px;font-weight:700;line-height:24px;color:var(--navy)}
.news-card p{position:absolute;top:402px;left:0;width:270px;font-size:14px;line-height:21px;color:var(--body)}

/* gallery */
.gallery-panel{left:575px;top:3870px;width:496px;height:422px;background:var(--navy)}

/* footer */
.site-footer{left:0;top:4390px;width:1200px;height:361px;background:var(--footer)}
.footer-nav a{position:absolute;top:227px;font-size:15px;font-weight:500;color:var(--ink);text-decoration:none}
.footer-legal a{position:absolute;top:280px;font-size:15px;color:var(--ink);text-decoration:none}
.social{position:absolute;top:93px;width:27px;height:27px;border-radius:50%;background:var(--ink)}
</style>
</head>
<body>

<header class="site-header abs">
  <div class="brand">Marvane Equity Partners</div>
  <nav class="main-nav">
    <a class="active" style="left:540px">HOME</a>
    <a style="left:632px">ABOUT US</a>
    <a style="left:754px">TEAM</a>
    <a style="left:842px">PORTFOLIO</a>
    <a style="left:973px">CONTACT US</a>
  </nav>
  <div class="phone-box">
    <svg width="28" height="28" viewBox="0 0 24 24" fill="none" stroke="#fff" stroke-width="1.5" stroke-linejoin="round"><path d="M5 3h4l2 5-2.5 1.5a11 11 0 0 0 6 6L16 13l5 2v4a2 2 0 0 1-2 2A16 16 0 0 1 3 5a2 2 0 0 1 2-2z"/></svg>
  </div>
</header>

<section class="hero abs" role="img" aria-label="Evening city skyline with lit towers">
  <h1 class="hero-title">Welcome to Marvane<br>Equity Partners</h1>
  <div class="btn-solid">Contact Us</div>
</section>

<section class="about">
  <div class="label abs about-label">About Us</div>
  <h2 class="abs about-heading">Marvane Equity Partners</h2>
  <p class="abs about-copy">Lorem ipsum dolor sit amet, consectetur adipiscing elit, sed do eiusmod tempor incididunt ut labore et dolore magna aliqua. Quis ipsum suspendisse ultrices gravida. Risus commodo viverra maecenas accumsaLorem ipsum dolor sit amet, consectetur adipiscing elit, sed do eiusmod tempor incididunt ut labore et dolore magna aliqs ipsum suspendisse.</p>
  <div class="stat" style="left:210px;width:200px"><b>30+</b><span>Years in Business</span></div>
  <div class="stat" style="left:480px;width:240px"><b>500+</b><span>Acquisitions to Date</span></div>
  <div class="stat" style="left:780px;width:250px"><b>$50B</b><span>Assets Under Management</span></div>
</section>

<section class="who">
  <div class="who-band abs"></div>
  <div class="label abs" style="left:127px;top:1252px">Who We Are</div>
  <h2 class="heading abs" style="left:127px;top:1298px;width:440px">A Trusted, Value-Added Partner for Your Business</h2>
  <p class="copy abs bar-copy" style="left:127px;top:1400px;width:430px">Lorem ipsum dolor sit amet, consectetur adipiscing elit, sed do eiusmod tempor incididunt ut labore et dolore magna aliqua. Quis ipsum suspendisse ultrices gravida. Risus commodo viverra maecenas accumsan lacus vel facilisis.</p>
  <div class="btn-line" style="left:127px;top:1559px;width:127px;height:43px">Read More</div>
  <div class="photo" role="img" aria-label="Two business people in conversation at a desk" style="left:627px;top:1237px;width:304px;height:365px;background:linear-gradient(135deg,#c9ccd1,#3b4d6d 60%,#1e2a40)"></div>
  <div class="photo" role="img" aria-label="Colleagues meeting around a table" style="left:955px;top:1237px;width:245px;height:241px;background:linear-gradient(135deg,#3a4254,#8a8f98 60%,#c7c1b8)"></div>
  <div class="photo" role="img" aria-label="Businessman standing in an office" style="left:955px;top:1509px;width:245px;height:319px;background:linear-gradient(160deg,#2a2b30,#4c4a48 50%,#1e2a3e)"></div>
</section>

<section class="services">
  <div class="label abs" style="left:127px;top:1868px">What We Do</div>
  <h2 class="heading abs" style="left:127px;top:1914px;width:360px">Explore Our Business Solutions</h2>

  <div class="service" style="left:127px">
    <svg width="64" height="64" viewBox="0 0 64 64" fill="none" stroke="#0b1f4f" stroke-width="3" stroke-linecap="round" stroke-linejoin="round"><path d="M4 30 22 14l10 10L52 4"/><path d="M42 4h10v10"/><path d="M6 60V42M16 60V34M26 60V38M36 60V44"/><path d="M58 36c-2-3-10-3-10 2s10 4 10 9-8 5-10 2M53 32v28"/></svg>
    <h3>Middle Market<br>Private Equity</h3>
    <p>Lorem ipsum dolor sitame conse ctetur adipiscing eli ed do eiusmod.</p>
  </div>
  <div class="service" style="left:376px">
    <svg width="64" height="64" viewBox="0 0 64 64" fill="none" stroke="#0b1f4f" stroke-width="3" stroke-linecap="round" stroke-linejoin="round"><rect x="4" y="14" width="50" height="40" rx="6"/><path d="M20 14V8h18v6"/><path d="M4 28h26"/><circle cx="44" cy="44" r="14" fill="#fff"/><path d="M44 36v9l6 3"/></svg>
    <h3>Small Business<br>Private Equity</h3>
    <p>Lorem ipsum dolor sitame conse ctetur adipiscing eli ed do eiusmod.</p>
  </div>
  <div class="service" style="left:623px">
    <svg width="64" height="64" viewBox="0 0 64 64" fill="none" stroke="#0b1f4f" stroke-width="3" stroke-linecap="round" stroke-linejoin="round"><circle cx="12" cy="10" r="7"/><path d="M2 32c0-8 5-12 10-12s10 4 10 12"/><path d="M30 34 58 4"/><path d="M48 4h10v10"/><path d="M30 60V46M40 60V36M50 60V26M60 60V18"/></svg>
    <h3 style="top:113px">Growth Capital</h3>
    <p>Lorem ipsum dolor sitame conse ctetur adipiscing eli ed do eiusmod.</p>
  </div>
  <div class="service" style="left:872px">
    <svg width="64" height="64" viewBox="0 0 64 64" fill="none" stroke="#0b1f4f" stroke-width="3" stroke-linecap="round" stroke-linejoin="round"><path d="M14 20c4-6 12-9 22-8 10 1 18 8 18 18 0 6-3 10-6 13v9h-8v-5h-12v5h-8v-8c-4-2-7-5-8-9H6V25h6z"/><circle cx="22" cy="26" r="1.5" fill="#0b1f4f"/><path d="M28 12c0-4 3-7 7-7s7 3 7 7"/></svg>
    <h3 style="top:113px">Private Debt</h3>
    <p>Lorem ipsum dolor sitame conse ctetur adipiscing eli ed do eiusmod.</p>
  </div>
</section>

<section class="why">
  <div class="why-band abs"></div>
  <div class="photo" role="img" aria-label="Glass skyscrapers seen from below against blue sky" style="left:146px;top:2414px;width:383px;height:548px;background:linear-gradient(160deg,#dfe8f2,#6f9ccc 40%,#2f5d96 70%,#8d8a86)"></div>
  <div class="label abs" style="left:647px;top:2517px">Why Choose Us?</div>
  <h2 class="heading abs" style="left:647px;top:2562px">How We Create Value</h2>
  <p class="copy abs bar-copy" style="left:647px;top:2636px;width:430px">Lorem ipsum dolor sit amet, consectetur adipiscing elit, sed do eiusmod tempor incididunt ut labore et dolore magna aliqua. Quis ipsum suspendisse ultrices gravida. Risus commodo viverra maecenas accumsan lacus vel facilisis.</p>
  <div class="btn-line" style="left:647px;top:2792px;width:168px;height:43px">Our Companies</div>
  <div class="btn-line" style="left:828px;top:2792px;width:134px;height:43px">Our Impact</div>
</section>

<section class="news">
  <div class="label abs" style="left:127px;top:3092px">News</div>
  <h2 class="heading abs" style="left:127px;top:3128px">Latest News &amp; Insights</h2>
  <svg class="abs" style="left:993px;top:3138px" width="82" height="20" viewBox="0 0 82 20" fill="none" stroke-linecap="round" stroke-linejoin="round" stroke-width="2"><path d="M34 10H2M10 3 2 10l8 7" stroke="#9aa0aa"/><path d="M48 10h32M72 3l8 7-8 7" stroke="#101a33"/></svg>

  <article class="news-card" style="left:127px">
    <div class="photo" role="img" aria-label="Hands reviewing financial charts on paper" style="background:linear-gradient(135deg,#9fa6b1,#d9dde3 50%,#4e5a6e)"></div>
    <h4>Lorem ipsum dolor sit amet consectetur</h4>
    <p>Lorem ipsum dolor sit amecse ctetur adipiscing elit, sed dius mod tempor incididun.</p>
  </article>
  <article class="news-card" style="left:422px">
    <div class="photo" role="img" aria-label="Businesswoman speaking in a meeting" style="background:linear-gradient(135deg,#343841,#7b7873 50%,#c9c6c2)"></div>
    <h4>Lorem ipsum dolor sit amet consectetur</h4>
    <p>Lorem ipsum dolor sit amecse ctetur adipiscing elit, sed dius mod tempor incididun.</p>
  </article>
  <article class="news-card" style="left:717px">
    <div class="photo" role="img" aria-label="Hand holding a pen over a laptop" style="background:linear-gradient(135deg,#3e4a5e,#8b94a3 50%,#2a3140)"></div>
    <h4>Lorem ipsum dolor sit amet consectetur</h4>
    <p>Lorem ipsum dolor sit amecse ctetur adipiscing elit, sed dius mod tempor incididun.</p>
  </article>
  <article class="news-card" style="left:1014px">
    <div class="photo" role="img" aria-label="Businesswoman seated at a table with coffee" style="background:linear-gradient(135deg,#4a4e56,#9a948c 50%,#d4d0ca)"></div>
    <h4>Lorem ipsum dolor sit amet consectetur</h4>
    <p>Lorem ipsum dolor sit amecse ctetur adipiscing elit, sed dius mod tempor incididun.</p>
  </article>
  <div class="abs" style="left:127px;top:3780px;width:946px;height:2px;background:var(--rule)"></div>
</section>

<section class="gallery">
  <div class="photo" role="img" aria-label="Advisor meeting with an older client reviewing documents" style="left:127px;top:3870px;width:448px;height:422px;background:linear-gradient(135deg,#e8e6e2,#b9ad9c 50%,#5c5a5c)"></div>
  <div class="gallery-panel abs"></div>
  <div class="label abs" style="left:647px;top:3954px;color:#a6acb9">Gallery</div>
  <h2 class="heading abs" style="left:647px;top:3990px;color:var(--white)">Portfolio Highlight</h2>
  <p class="copy abs" style="left:647px;top:4060px;width:360px;color:#e6e9ef">Lorem ipsum dolor sit amet, consectetur adipiscing elit, sed do eiusmod tempor incididunt ut labore et dolore magna aliqmod tempor incididunt ut labore et dolore mua.</p>
  <div class="abs" style="left:647px;top:4179px;font-size:14px;font-weight:700;color:var(--white);display:flex;align-items:center;gap:10px">Read More
    <svg width="24" height="12" viewBox="0 0 24 12" fill="none" stroke="#fff" stroke-width="1.6" stroke-linecap="round"><path d="M1 6h21M17 1l5 5-5 5"/></svg>
  </div>
</section>

<footer class="site-footer abs">
  <div class="brand" style="left:127px;top:82px;font-size:24px">Marvane Equity Partners</div>
  <span class="social" style="left:933px"></span>
  <span class="social" style="left:970px"></span>
  <span class="social" style="left:1007px"></span>
  <span class="social" style="left:1044px"></span>
  <div class="abs" style="left:127px;top:164px;width:946px;height:1px;background:#c9ccd2"></div>
  <nav class="footer-nav">
    <a style="left:127px">HOME</a>
    <a style="left:224px">ABOUT US</a>
    <a style="left:353px">TEAM</a>
    <a style="left:446px">PORTFOLIO</a>
    <a style="left:583px">CONTACT US</a>
  </nav>
  <nav class="footer-legal">
    <a style="left:127px">Investor Portal</a>
    <a style="left:274px">Privacy</a>
    <a style="left:366px">Terms</a>
    <a style="left:449px">Site Map</a>
  </nav>
  <div class="abs" style="left:700px;width:373px;top:280px;text-align:right;font-size:15px;color:var(--ink)">Copyright © 2025 All Rights Are Reserved.</div>
</footer>

</body>
</html>
```